Project Manager Business Card for Top Architectural Firm

Update and design a stunning Senior Project Manager Business Card

MARCO T. DRUMMOND II
Senior Project Manager

H A L C Y O N
A R C H I T E C T U R E L L C.
www.HalcyonGrandEstates.example
4127 NW 52nd Ter. Suite 2308
Miami, FL 33148
C: (305) 555-0184
mdrummond.halcyongrandestates@mailbox.example

Looking to have the logo to be UV Spot ink printed and to be prominent.

Target Market(s)

High end real estate architecture construction

Industry/Entity Type

Architect

Contact Information for Business Card

MARCO T. DRUMMOND II
Senior Project Manager

H A L C Y O N
Miami, FL 33148
C: (305) 555-0184

Font styles to use
Sans Serif

Colors

Designer to choose colors to be used in the design.

Requirements
Must have
• Prominent Logo

```html
<!DOCTYPE html>
<html lang="en">
<head>
<meta charset="utf-8">
<title>Halcyon Architecture — Business Card</title>
<link rel="stylesheet" href="https://fonts.googleapis.com/css2?family=Oswald:wght@200;300&family=Roboto:wght@300;400&display=swap">
<style>
  :root {
    --backdrop: #3a3b3e;
    --card: #222326;
    --card-edge: #2c2d31;
    --ink: #f4f4f4;
    --muted: #a9abb0;
    --accent-warm: #e0683a;
    --accent-cool: #2b8fd8;
    --mark: #2b8fd8;
  }
  * { box-sizing: border-box; margin: 0; padding: 0; }
  html, body { width: 799px; height: 1200px; overflow: hidden; }
  body {
    background: var(--backdrop);
    display: flex;
    flex-direction: column;
    align-items: center;
    justify-content: center;
    gap: 70px;
    font-family: "Roboto", sans-serif;
  }
  .card {
    position: relative;
    width: 640px;
    height: 366px;
    background: var(--card);
    border: 1px solid var(--card-edge);
    border-radius: 4px;
    box-shadow: 0 12px 30px rgba(0,0,0,.45);
    overflow: hidden;
  }
  .brand { display: flex; align-items: center; gap: 18px; }
  .brand-dot {
    border-radius: 50%;
    background: var(--mark);
    flex: none;
  }
  .brand-text {
    font-family: "Oswald", sans-serif;
    font-weight: 200;
    color: var(--ink);
    line-height: 1;
  }
  .brand-name { display: block; letter-spacing: .06em; }
  .brand-sub { display: block; letter-spacing: .32em; margin-top: 6px; }

  /* front */
  .card-front { display: flex; align-items: center; justify-content: center; }
  .card-front .brand-dot { width: 74px; height: 74px; }
  .card-front .brand-name { font-size: 72px; }
  .card-front .brand-sub { font-size: 13px; }

  /* back */
  .card-back { padding: 38px 46px; }
  .card-back .brand-dot { width: 50px; height: 50px; }
  .card-back .brand-name { font-size: 46px; }
  .card-back .brand-sub { font-size: 10px; }
  .person { margin-top: 26px; }
  .person-name {
    font-family: "Oswald", sans-serif;
    font-weight: 300;
    font-size: 30px;
    letter-spacing: .04em;
    color: var(--ink);
    line-height: 1.1;
  }
  .person-title {
    font-size: 15px;
    font-weight: 300;
    color: var(--muted);
    letter-spacing: .04em;
    margin-top: 4px;
  }
  .contacts { list-style: none; margin-top: 20px; }
  .contacts li {
    display: flex;
    align-items: flex-start;
    gap: 12px;
    font-size: 14px;
    color: var(--ink);
    line-height: 1.45;
  }
  .contacts svg { width: 13px; height: 13px; margin-top: 3px; flex: none; fill: var(--ink); }
  .accent-rule {
    position: absolute;
    left: 46px;
    bottom: 26px;
    width: 168px;
    height: 2px;
    background: linear-gradient(90deg, var(--accent-warm), var(--accent-cool));
  }
</style>
</head>
<body>

<section class="card card-front" aria-label="Card front">
  <div class="brand">
    <span class="brand-dot"></span>
    <div class="brand-text">
      <span class="brand-name">H A L C Y O N</span>
      <span class="brand-sub">A R C H I T E C T U R E L L C.</span>
    </div>
  </div>
</section>

<section class="card card-back" aria-label="Card back">
  <div class="brand">
    <span class="brand-dot"></span>
    <div class="brand-text">
      <span class="brand-name">H A L C Y O N</span>
      <span class="brand-sub">A R C H I T E C T U R E L L C.</span>
    </div>
  </div>

  <div class="person">
    <p class="person-name">MARCO T. DRUMMOND II</p>
    <p class="person-title">Senior Project Manager</p>
  </div>

  <ul class="contacts">
    <li>
      <svg viewBox="0 0 16 16"><path d="M3.5 1h3l1.2 3.6-1.9 1.3a9 9 0 0 0 4.3 4.3l1.3-1.9L15 9.5v3c0 .8-.7 1.5-1.5 1.5A12.5 12.5 0 0 1 2 2.5C2 1.7 2.7 1 3.5 1z"/></svg>
      (305) 555-0184
    </li>
    <li>
      <svg viewBox="0 0 16 16"><path d="M1 3h14v10H1zM2 4.2V12h12V4.2L8 8.6z"/><path d="M2 3.6 8 8l6-4.4z"/></svg>
      mdrummond.halcyongrandestates@mailbox.example
    </li>
    <li>
      <svg viewBox="0 0 16 16"><path d="M8 1a7 7 0 1 0 0 14A7 7 0 0 0 8 1zm0 1.3c.8 0 1.8 1.6 2.1 4.2H5.9C6.2 3.9 7.2 2.3 8 2.3zM2.4 7.5h2.2c0 .4 0 .7 0 1H2.4zm9 0h2.2v1h-2.2zM5.9 9.5h4.2c-.3 2.6-1.3 4.2-2.1 4.2s-1.8-1.6-2.1-4.2z"/></svg>
      www.HalcyonGrandEstates.example
    </li>
    <li>
      <svg viewBox="0 0 16 16"><path d="M8 1a5 5 0 0 0-5 5c0 3.8 5 9 5 9s5-5.2 5-9a5 5 0 0 0-5-5zm0 7a2 2 0 1 1 0-4 2 2 0 0 1 0 4z"/></svg>
      <span>4127 NW 52nd Ter. Suite 2308<br>Miami, FL 33148</span>
    </li>
  </ul>

  <div class="accent-rule"></div>
</section>

</body>
</html>
```